Poster for Starlette-style Christmas music and dance show.

I need a poster for a Christmas music and dance show styled after the Harbor Lane Starlettes. Attached are samples of posters for previous years. I like the font style and colors of the blue one. The design should contain an ornament design with dancers dancing on it. The dancers should be cartoon style, not photo real. A sample is attached.
The poster MUST contain the PelMUSE logo, sponsor logos, the dates (December 12-13, 2015), the location (Lyle & Ruth Danvers Theatre, 4817 Quillberry Bend, Lakeway, TX), PelMUSE contact info (www.pel-muse.example and 555-307-4162 ext 204), and "Directed and Choreographed by Colin Ashby."
Logos are all attached. Finalized files needed in sizes: 12x18, 4x6, and 30x48 inches.

Target Market(s)

Community Theatre patrons

Industry/Entity Type

Radio

Font styles to use
Serif

Colors
0792cd
33a6d7
85cae6
ecf7fb
ffffff

Requirements
Must have
• PelMUSE logo (attached)
• sponsor logos: Neva Orr Photography, Pruitt Dentistry, Bluefin Grill, Up Tempo (attached)
• Show dates: December 12-13, 2015)
• Show Location: Lyle & Ruth Danvers Theatre, 4817 Quillberry Bend, Lakeway, TX)
• PelMUSE contact info: www.pel-muse.example and 555-307-4162 ext 204
• "Directed and Choreographed by Colin Ashby"
• An ornament design with dancers on it. The dancers should be cartoon style, not photo real. A sample of a dancer graphic is attached.
Nice to have
• snowflakes or other winter themes

```html
<!DOCTYPE html>
<html lang="en">
<head>
<meta charset="utf-8">
<title>Holiday Extravaganza – PelMUSE</title>
<link rel="stylesheet" href="https://fonts.googleapis.com/css2?family=Lora:wght@400;700&family=Rokkitt:wght@600;800&family=Great+Vibes&display=swap">
<style>
  :root {
    --blue-deep: #0792cd;
    --blue-mid: #33a6d7;
    --blue-soft: #85cae6;
    --blue-mist: #ecf7fb;
    --white: #ffffff;
    --wood-dark: #0b4f6e;
    --wood-light: #2a8fb3;
    --ribbon-red: #c8142c;
    --ink: #3d3d3d;
    --ink-soft: #6b6b6b;
  }
  * { margin: 0; padding: 0; box-sizing: border-box; }
  html, body { width: 900px; height: 1200px; overflow: hidden; background: var(--white); }
  .poster {
    position: relative; width: 900px; height: 1200px; overflow: hidden;
    background: var(--white); font-family: "Lora", Georgia, serif; color: var(--ink);
  }
  .presenter {
    position: absolute; top: 26px; left: 0; width: 100%; text-align: center;
  }
  .presenter-name {
    font-family: "Lora", Georgia, serif; font-weight: 700; font-size: 56px;
    color: var(--blue-deep); letter-spacing: 1px; line-height: 1;
  }
  .presenter-tagline {
    margin-top: 8px; font-size: 13px; letter-spacing: 3px; text-transform: uppercase;
    color: var(--blue-deep);
  }
  .hero {
    position: absolute; top: 122px; left: 72px; width: 756px; height: 570px;
    border-radius: 40px;
    background:
      radial-gradient(ellipse at center, rgba(255,255,255,0) 58%, rgba(255,255,255,0.95) 80%),
      linear-gradient(180deg, var(--wood-light) 0%, var(--blue-deep) 45%, var(--wood-dark) 100%);
  }
  .hero-ribbon {
    position: absolute; top: 128px; left: 0; width: 100%; height: 26px;
    background: var(--ribbon-red);
  }
  .hero-bow {
    position: absolute; top: 84px; left: 318px; width: 120px; height: 110px;
    border-radius: 50%;
    background: radial-gradient(circle, #e0324a 0%, var(--ribbon-red) 60%, rgba(200,20,44,0) 72%);
  }
  .show-title {
    position: absolute; top: 190px; left: 0; width: 100%; text-align: center;
    font-family: "Rokkitt", Georgia, serif; font-weight: 800; font-size: 124px;
    letter-spacing: 6px; color: var(--white); line-height: 1;
    text-shadow: 0 3px 6px rgba(0,0,0,0.25);
  }
  .show-subtitle {
    position: absolute; top: 300px; left: 0; width: 100%; text-align: center;
    font-family: "Great Vibes", cursive; font-size: 58px; color: var(--ribbon-red); line-height: 1;
  }
  .dancers {
    position: absolute; top: 372px; left: 190px; width: 376px; height: 150px;
    border-radius: 20px;
    background: linear-gradient(180deg, rgba(255,255,255,0.85), rgba(236,247,251,0.55));
  }
  .credits {
    position: absolute; top: 704px; left: 0; width: 100%; text-align: center;
  }
  .credit-label {
    font-family: "Great Vibes", cursive; font-size: 30px; color: var(--ink-soft); line-height: 1.1;
  }
  .credit-value {
    font-family: "Lora", Georgia, serif; font-weight: 700; font-size: 30px;
    letter-spacing: 1px; color: var(--ink); line-height: 1.2;
  }
  .credit-value.small { font-size: 25px; letter-spacing: 0; }
  .credit-value + .credit-label { margin-top: 4px; }
  .contact-bar {
    position: absolute; top: 932px; left: 90px; width: 720px; height: 40px;
    background: var(--blue-deep); color: var(--white);
    font-size: 22px; line-height: 40px; text-align: center; letter-spacing: 0.5px;
  }
  .sponsors-label {
    position: absolute; top: 984px; left: 0; width: 100%; text-align: center;
    font-family: "Great Vibes", cursive; font-size: 28px; color: var(--ink-soft);
  }
  .sponsor-row {
    position: absolute; left: 60px; width: 780px;
    display: flex; justify-content: space-around; align-items: center;
  }
  .sponsor-row.major { top: 1030px; }
  .sponsor-row.local { top: 1112px; }
  .sponsor {
    display: flex; align-items: center; gap: 10px;
    font-family: "Lora", Georgia, serif; font-weight: 700; font-size: 18px;
    color: var(--ink); max-width: 200px; line-height: 1.15;
  }
  .sponsor-mark { flex: none; width: 34px; height: 34px; background: var(--blue-deep); }
  .sponsor-mark.round { border-radius: 50%; }
  .sponsor.accent { color: var(--blue-deep); }
</style>
</head>
<body>
<div class="poster">
  <header class="presenter">
    <div class="presenter-name">PelMUSE</div>
    <div class="presenter-tagline">Broadway Company Presents</div>
  </header>

  <section class="hero" role="img" aria-label="Blue wooden plank backdrop framed by snowy pine branches and falling snow">
    <div class="hero-ribbon"></div>
    <div class="hero-bow" role="img" aria-label="Red ribbon bow"></div>
    <h1 class="show-title">HOLIDAY</h1>
    <div class="show-subtitle">Extravaganza</div>
    <div class="dancers" role="img" aria-label="White cartoon silhouettes of a line of dancers in a kick line"></div>
  </section>

  <section class="credits">
    <div class="credit-label">Directed and Choreographed by</div>
    <div class="credit-value">COLIN ASHBY</div>
    <div class="credit-label">Date</div>
    <div class="credit-value">DECEMBER 12-13, 2015</div>
    <div class="credit-label">Location</div>
    <div class="credit-value small">Lyle &amp; Ruth Danvers Theatre, 4817 Quillberry Bend, Lakeway, TX)</div>
  </section>

  <div class="contact-bar">www.pel-muse.example | 555-307-4162 ext 204</div>

  <div class="sponsors-label">Sponsors</div>

  <div class="sponsor-row major">
    <div class="sponsor"><span class="sponsor-mark round"></span>Lone Star Arts Council</div>
    <div class="sponsor"><span class="sponsor-mark"></span>Art Forward</div>
    <div class="sponsor">National Arts Fund</div>
  </div>

  <div class="sponsor-row local">
    <div class="sponsor"><span class="sponsor-mark"></span>Bluefin Grill</div>
    <div class="sponsor">Neva Orr Photography</div>
    <div class="sponsor accent">Grove &amp; Press</div>
    <div class="sponsor accent"><span class="sponsor-mark round"></span>Up Tempo</div>
    <div class="sponsor">Pruitt Dentistry</div>
  </div>
</div>
</body>
</html>
```